we are starting an online childrens clothing store, The Kettle Beneath The Hill, and require an easy to navigate, simple and elegant in design. we will suply our own domain and company logo.

Target Market(s)

Familys with children aged 0 to 8

Industry/Entity Type

Clothing

Requirements
Must have
• easy to navigate,
our company logo on the header of each page
easy two step checkout with paypal access.
easy to modify and add to site by us at no or minimal cost.
6 pages, home page, boys clothing, girls clothing, our brands, about us, contact.
Ad Space
Friendwall link
Should not have
• pop up ads
dark colours

```html
<!DOCTYPE html>
<html lang="en">
<head>
<meta charset="utf-8">
<title>Children's Clothing Store</title>
<link href="https://fonts.googleapis.com/css2?family=Oswald:wght@400;500&family=Open+Sans:wght@400;600&display=swap" rel="stylesheet">
<style>
:root{
  --page:#eeedf9;
  --lilac:#b9b1ea;
  --lilac-soft:#c3bcee;
  --violet:#9a8ade;
  --violet-deep:#8f7fd8;
  --head-text:#a08fe0;
  --white:#ffffff;
  --green:#7bc820;
  --green-btn:#82cf1e;
  --footer-text:#3f3a66;
  --band:#221660;
  --row:#e3e0f8;
  --photo-light:#ecebef;
  --photo-grey:#d6d5db;
  --photo-pastel:#ebe2e4;
  --photo-navy:#3a4670;
  --photo-pink:#f0cdd3;
  --photo-dark:#9c9ba2;
}
*{box-sizing:border-box;margin:0;padding:0}
html,body{width:909px;height:1200px;overflow:hidden}
body{background:var(--page);position:relative;font-family:"Open Sans",Arial,sans-serif;color:var(--violet)}
.abs{position:absolute}
.display{font-family:"Oswald",sans-serif;text-transform:uppercase}
.brand{left:84px;top:36px;font-size:21px;color:var(--head-text);font-weight:500;letter-spacing:.2px}
.currency-label{left:662px;top:36px;font-size:8px;color:var(--violet)}
.currency-box{left:702px;top:33px;width:67px;height:16px;border:1px solid var(--lilac);background:var(--white);font-size:7px;color:var(--violet);padding:2px 0 0 18px}
.currency-box .arrow{position:absolute;right:0;top:0;width:13px;height:14px;border-left:1px solid var(--lilac)}
.account{left:638px;top:69px;font-size:9px;color:var(--violet)}
.cart-bubble{left:777px;top:39px;width:45px;height:45px;border-radius:50%;background:radial-gradient(circle at 40% 35%,#eef3fb,#b9cce8);box-shadow:0 2px 3px rgba(80,80,140,.25)}
.cart-bubble svg{position:absolute;left:10px;top:11px}
.nav{left:84px;top:105px;width:741px;height:43px;background:var(--lilac);display:flex}
.nav a{color:var(--white);font-size:13px;font-weight:500;text-decoration:none;display:flex;align-items:center;justify-content:center;border-right:1px solid #a99fe2;height:100%}
.nav a:last-child{border-right:none}
.hero{left:84px;top:176px;width:499px;height:288px;background:linear-gradient(180deg,#f4f1f1,#e9e3ea)}
.store{left:614px;width:208px;height:131px;background:linear-gradient(90deg,#e9e8ee,#fafafc);border-radius:6px;overflow:hidden}
.store .title{position:absolute;left:6px;top:7px;font-size:23px;line-height:26px;color:var(--violet-deep);font-weight:500}
.store .shop{position:absolute;left:8px;top:89px;font-size:12px;color:var(--violet-deep);font-weight:500}
.store .photo{position:absolute;left:64px;top:0;width:144px;height:131px}
.boys-store{top:176px}.boys-store .photo{background:var(--photo-grey)}
.girls-store{top:333px}.girls-store .title{top:11px}.girls-store .shop{top:92px}
.girls-store .photo{background:var(--photo-pastel)}
.panel{background:var(--white);border-radius:4px}
.side-head{height:34px;background:var(--violet);color:var(--white);font-size:17px;font-weight:500;padding-left:14px;line-height:34px;border-radius:2px}
.cart-box{left:84px;top:493px;width:177px;height:157px}
.cart-box .icon{position:absolute;right:9px;top:3px;width:28px;height:28px;border-radius:50%;background:radial-gradient(circle at 40% 35%,#eef3fb,#b9cce8)}
.cart-box .icon svg{position:absolute;left:6px;top:7px}
.cart-body{padding:12px 15px 0 15px;font-size:10px;color:var(--violet)}
.cart-row{display:flex;justify-content:space-between;background:var(--row);height:18px;line-height:18px;padding:0 4px;margin-top:4px;font-size:10.5px}
.cart-link{display:flex;align-items:center;gap:10px;margin-top:5px;font-size:10px}
.cart-link i{display:block;width:12px;height:8px;background:#a99ce3}
.offers{left:84px;top:660px;width:177px;height:372px}
.offer-img{position:absolute;border-radius:4px}
.offer-name{position:absolute;width:177px;text-align:center;font-size:12px;color:#b27ad6}
.offer-price{position:absolute;width:177px;text-align:center;font-size:11.5px;color:var(--green)}
.offer-price s{color:#999;margin-left:6px}
.main{left:270px;top:492px;width:555px;height:540px}
.sec-head{position:absolute;left:21px;font-size:16px;font-weight:500;color:var(--head-text)}
.rule{position:absolute;left:0;width:555px;height:5px;background:var(--page)}
.product{position:absolute;width:155px}
.product .img{width:150px;height:120px;border:1px solid #ddd}
.product .line{height:1px;background:#ddd;margin-top:16px}
.product .cap{font-size:8px;color:#a897e6;text-align:center;margin-top:12px;white-space:nowrap}
.product .buy{display:flex;justify-content:space-between;align-items:center;margin-top:22px}
.product .price{font-size:12px;color:var(--green)}
.product .view{background:var(--green-btn);color:var(--white);font-size:9.5px;padding:4px 6px;border-radius:2px}
.footer{left:84px;top:1054px;width:741px;height:118px;background:var(--lilac-soft)}
.fcol{position:absolute;top:10px;color:var(--footer-text)}
.fcol h3{font-size:14px;font-weight:600;margin-bottom:6px;padding-left:14px}
.fcol li{list-style:none;font-size:10px;line-height:17px}
.fcol li b{font-weight:600;margin-right:8px}
.social li{display:flex;align-items:center;gap:9px;margin-bottom:5px;font-size:10px;line-height:20px}
.social i{display:block;width:20px;height:20px;background:#4b4a5a}
.copy{left:84px;top:1172px;width:741px;height:28px;background:var(--band);color:var(--white);font-size:10px;line-height:28px;padding-left:31px}
</style>
</head>
<body>

<div class="abs display brand">Your Logo Here</div>
<div class="abs display currency-label">Currency</div>
<div class="abs display currency-box">Dollar<span class="arrow"></span></div>
<div class="abs account">Welcome, (Log In) &nbsp;Your Account</div>
<div class="abs cart-bubble">
  <svg width="26" height="22" viewBox="0 0 26 22"><path d="M1 3h4l3 11h12l3-8H7" fill="none" stroke="#2a4f9a" stroke-width="2.2" stroke-linejoin="round"/><circle cx="10" cy="18" r="2" fill="#2a4f9a"/><circle cx="19" cy="18" r="2" fill="#2a4f9a"/></svg>
</div>

<nav class="abs nav display">
  <a style="width:75px">Home</a>
  <a style="width:107px">Boys Clothing</a>
  <a style="width:110px">Girls Clothing</a>
  <a style="width:107px">Our Brands</a>
  <a style="width:79px">About Us</a>
  <a style="width:80px">About Us</a>
  <a style="width:80px">Contact Us</a>
  <a style="width:103px">Ad Space</a>
</nav>

<div class="abs hero" role="img" aria-label="Photo: group of children in colourful winter clothes walking together"></div>

<div class="abs store boys-store">
  <div class="title display">Boys<br>Store</div>
  <div class="shop display">Shop Now</div>
  <div class="photo" role="img" aria-label="Photo: four boys in jackets and jeans"></div>
</div>
<div class="abs store girls-store">
  <div class="title display">Girls<br>Store</div>
  <div class="shop display">Shop Now</div>
  <div class="photo" role="img" aria-label="Photo: four girls in pastel party dresses"></div>
</div>

<aside class="abs panel cart-box">
  <div class="side-head display">Cart</div>
  <div class="icon"><svg width="16" height="14" viewBox="0 0 26 22"><path d="M1 3h4l3 11h12l3-8H7" fill="none" stroke="#2a4f9a" stroke-width="2.6"/><circle cx="10" cy="18" r="2.4" fill="#2a4f9a"/><circle cx="19" cy="18" r="2.4" fill="#2a4f9a"/></svg></div>
  <div class="cart-body display">
    <div style="margin-bottom:8px">No Products</div>
    <div class="cart-row"><span>Shipping</span><span>$0.00</span></div>
    <div class="cart-row"><span>Total</span><span>$0.00</span></div>
    <div class="cart-link" style="margin-top:10px"><i></i>Cart</div>
    <div class="cart-link"><i></i>Check Out</div>
  </div>
</aside>

<aside class="abs panel offers">
  <div class="side-head display" style="text-align:center;padding:0">Special Offers</div>
  <div class="offer-img" style="left:44px;top:42px;width:90px;height:106px;background:var(--photo-navy)" role="img" aria-label="Photo: boy wearing a navy sports jacket"></div>
  <div class="offer-name display" style="top:160px">Boys Jacket</div>
  <div class="offer-price" style="top:185px">$30.60<s>$36.00</s></div>
  <div class="offer-img" style="left:41px;top:214px;width:96px;height:94px;background:var(--photo-pink)" role="img" aria-label="Photo: pink satin girls fancy dress"></div>
  <div class="offer-name display" style="top:320px">Girls Fancy Dress</div>
  <div class="offer-price" style="top:346px">$30.60<s>$36.00</s></div>
</aside>

<main class="abs panel main">
  <h2 class="sec-head display" style="top:12px">Boys Clothing</h2>
  <div class="rule" style="top:42px"></div>

  <div class="product" style="left:25px;top:56px">
    <div class="img" role="img" aria-label="Photo: two boys in casual jackets and shorts" style="background:var(--photo-light)"></div>
    <div class="line"></div><div class="cap">Lorem ipsum duis interdum eget urna</div>
    <div class="buy"><span class="price">$25.00</span><span class="view">VIEW</span></div>
  </div>
  <div class="product" style="left:216px;top:56px">
    <div class="img" role="img" aria-label="Photo: three children in dark coats and boots" style="border:none;background:var(--photo-grey)"></div>
    <div class="line"></div><div class="cap" style="margin-top:6px">Consectetur adipiscing elit</div>
    <div class="buy" style="margin-top:28px"><span class="price">$17.00</span><span class="view">VIEW</span></div>
  </div>
  <div class="product" style="left:395px;top:56px">
    <div class="img" role="img" aria-label="Photo: grid of six boys in knitwear and jackets" style="border:none;background:var(--photo-grey)"></div>
    <div class="line"></div><div class="cap" style="margin-top:9px">Aenean sagittis sed congue leo</div>
    <div class="buy" style="margin-top:26px"><span class="price">$39.20</span><span class="view">VIEW</span></div>
  </div>

  <h2 class="sec-head display" style="top:289px">Girls Clothing</h2>
  <div class="rule" style="top:319px"></div>

  <div class="product" style="left:22px;top:333px">
    <div class="img" role="img" aria-label="Photo: four girls in pastel party dresses" style="border:none;background:var(--photo-pastel)"></div>
    <div class="line"></div><div class="cap" style="margin-top:14px">Lorem ipsum duis interdum eget urna</div>
    <div class="buy"><span class="price">$25.00</span><span class="view">VIEW</span></div>
  </div>
  <div class="product" style="left:216px;top:335px">
    <div class="img" role="img" aria-label="Photo: three children in dark coats and boots" style="border:none;background:var(--photo-grey)"></div>
    <div class="line"></div><div class="cap" style="margin-top:6px">Consectetur adipiscing elit</div>
    <div class="buy" style="margin-top:24px"><span class="price">$17.00</span><span class="view">VIEW</span></div>
  </div>
  <div class="product" style="left:395px;top:337px">
    <div class="img" role="img" aria-label="Photo: two girls in white dresses with pink sashes" style="border:none;background:var(--photo-dark)"></div>
    <div class="line"></div><div class="cap" style="margin-top:9px">Aenean sagittis sed congue leo</div>
    <div class="buy" style="margin-top:26px"><span class="price">$39.20</span><span class="view">VIEW</span></div>
  </div>
</main>

<footer class="abs footer">
  <div class="fcol" style="left:4px">
    <h3 style="padding-left:15px">Information</h3>
    <ul><li><b>&gt;&gt;</b>About Us</li><li><b>&gt;&gt;</b>Delivery Information</li><li><b>&gt;&gt;</b>Privacy Policy</li><li><b>&gt;&gt;</b>Terms and Conditions</li></ul>
  </div>
  <div class="fcol" style="left:228px">
    <h3 style="padding-left:0">Sitemap</h3>
    <ul><li><b>&gt;&gt;</b>Boys Clothing</li><li><b>&gt;&gt;</b>Girls Clothing</li><li><b>&gt;&gt;</b>Our Brands</li><li><b>&gt;&gt;</b>Contact Us</li></ul>
  </div>
  <div class="fcol" style="left:424px">
    <h3 style="padding-left:0">MY Cart</h3>
    <ul><li><b>&gt;&gt;</b>My Orders</li><li><b>&gt;&gt;</b>My Personal Info</li><li><b>&gt;&gt;</b>My Credit Slip</li><li><b>&gt;&gt;</b>My Voucher</li></ul>
  </div>
  <div class="fcol social" style="left:577px">
    <h3 style="padding-left:12px">Join Us</h3>
    <ul><li><i></i>Friendwall</li><li><i></i>Chirper</li><li><i></i>Workline</li></ul>
  </div>
</footer>
<div class="abs copy">All Rights Reserved/Copyright @Meadowlark Networks 2012</div>

</body>
</html>
```